Wordpress Design for a Private Label BBQ Brand

For our new brand, we'd need a new Wordpress website. We'd prefer to run the website on Wordpress

We'd like to include the following
- space for description of the brand
- space for product portfolio (not a shop!)
- space for socials
- space for support
- space for contact

```html
<!DOCTYPE html>
<html lang="en">
<head>
<meta charset="utf-8">
<title>Fornace – Brand &amp; Website Design</title>
<link rel="stylesheet" href="https://fonts.googleapis.com/css2?family=Crimson+Pro:wght@500;600;700&family=Nunito+Sans:wght@400;600;700&display=swap">
<style>
:root{
  --ink:#1e1e1e;
  --red:#be1622;
  --orange:#ed691c;
  --cream:#fdf3ee;
  --board:#fcf3f0;
  --white:#ffffff;
  --muted:#8a7f7b;
  --serif:'Crimson Pro', Georgia, serif;
  --sans:'Nunito Sans', Arial, sans-serif;
}
*{box-sizing:border-box;margin:0;padding:0}
html,body{width:1200px;height:3475px;overflow:hidden}
body{background:var(--board);font-family:var(--sans);color:var(--ink);position:relative}
.abs{position:absolute}

/* Brand board */
.brand-mark{left:198px;top:140px;display:flex;align-items:center;gap:10px}
.brand-mark .dot{width:30px;height:30px;border-radius:50%;background:var(--orange)}
.brand-mark span{font-family:var(--serif);font-weight:700;font-size:40px;letter-spacing:1px}
.divider{width:1px;height:90px;background:#e6d8d2}
.board-title{font-family:var(--serif);font-weight:700;font-size:30px}
.font-list p{color:var(--muted);line-height:26px}
.font-list .f1{font-family:var(--serif);font-size:24px;font-weight:500}
.font-list .f2{font-size:16px;font-weight:600}
.font-list .f3{font-size:16px}
.swatches{display:flex;gap:14px}
.swatch{text-align:center;font-size:11px;color:#555}
.swatch i{display:block;width:40px;height:40px;border-radius:50%;margin-bottom:6px}

/* Page */
.page{left:221px;top:291px;width:793px;height:3075px;background:var(--white)}
.nav{left:241px;top:291px;width:773px;height:53px;display:flex;align-items:center;justify-content:space-between}
.nav-logo{font-family:var(--serif);font-weight:700;font-size:18px;display:flex;align-items:center;gap:5px}
.nav-logo i{width:12px;height:12px;border-radius:50%;background:var(--orange)}
.nav-links{display:flex;align-items:center;gap:22px;font-size:9px}
.btn{display:inline-block;font-size:8px;font-weight:700;padding:8px 16px;text-decoration:none}
.btn-solid{background:linear-gradient(90deg,var(--red),var(--orange));color:#fff}
.btn-line{border:1px solid var(--red);color:var(--red);background:#fff}
.socials{display:flex;gap:5px}
.socials i{width:7px;height:7px;background:var(--ink);border-radius:1px}

.photo{display:block}
.hero-photo{left:241px;top:344px;width:773px;height:451px;background:linear-gradient(120deg,#8fa07a 0%,#b9b89a 35%,#c48a54 65%,#6f5b48 100%)}
.hero-card{left:262px;top:597px;width:280px;height:178px;background:#fff;padding:28px 31px}
.hero-card h1{font-family:var(--serif);font-weight:700;font-size:30px;line-height:34px}
.hero-card .btn{margin-top:24px}

.feature{left:221px;top:815px;width:774px;height:405px;background:linear-gradient(90deg,#fbf1ed 0%,#f6e6df 55%,#efdcd3 100%)}
.grill-photo{left:320px;top:870px;width:216px;height:296px;background:linear-gradient(180deg,#f4d6cf 0%,#e9c9c0 100%)}
.feature-text{left:686px;top:880px;width:230px}
h2.title{font-family:var(--serif);font-weight:700;font-size:24px;line-height:28px}
.body-s{font-size:9px;line-height:16px;color:var(--muted)}
.ticks{list-style:none;margin:10px 0}
.ticks li{font-size:8.5px;display:flex;align-items:center;gap:7px;height:19px}
.ticks svg{flex:none}

.dark{left:241px;top:1240px;width:773px;height:394px;background:linear-gradient(90deg,#1e1e1e 0%,#2a1a14 55%,#1e1e1e 100%)}
.dark-text{left:329px;top:1306px;width:230px;color:#fff}
.dark-text .body-s{color:#bdb3ad}
.dark-text .ticks li{color:#e8ded9}
.dark-photo{left:681px;top:1312px;width:314px;height:381px;background:linear-gradient(180deg,#c9a47c 0%,#8a6246 45%,#3a2a22 75%,#1e1e1e 100%)}

.section-head{text-align:center;width:793px;left:221px}
.section-head i{display:block;width:14px;height:14px;border-radius:50%;background:var(--orange);margin:0 auto 12px}
.section-head h2{font-family:var(--serif);font-weight:700;font-size:28px}
.card{top:1844px;width:173px;height:208px;background:var(--cream)}
.card .product{position:absolute;left:20px;top:24px;width:133px;height:148px;background:linear-gradient(180deg,#f6e6df,#ecd9d1)}
.card .tag{position:absolute;right:10px;bottom:8px;font-family:var(--serif);font-weight:700;font-size:7px}
.dots{left:605px;top:2085px;display:flex;gap:5px}
.dots i{width:5px;height:5px;border-radius:50%;background:#f0c8b8}
.dots i.on{background:var(--orange)}

.mission-strip{left:221px;top:2151px;width:31px;height:395px;background:#b3b3b3}
.mission-photo{left:252px;top:2151px;width:365px;height:395px;background:linear-gradient(160deg,#7d8f5a 0%,#c69a74 40%,#4a4440 75%,#9b7d5c 100%)}
.mission{left:617px;top:2170px;width:378px;height:376px;background:linear-gradient(135deg,var(--red),var(--orange));color:#fff;text-align:center;padding:58px 50px}
.center-block i.mk{display:block;width:14px;height:14px;border-radius:50%;margin:0 auto 12px}
.center-block h2{font-family:var(--serif);font-weight:700;font-size:30px;margin-bottom:18px}
.center-block p{font-size:9px;line-height:16px;margin-bottom:12px}
.mission .btn-white{background:#fff;color:var(--red)}

.values{left:240px;top:2546px;width:377px;height:368px;background:var(--cream);text-align:center;padding:52px 54px}
.values p{color:var(--muted)}
.values-photo{left:617px;top:2546px;width:397px;height:395px;background:linear-gradient(150deg,#7e9a5a 0%,#5d7a3e 40%,#3a3a36 70%,#9a8a6e 100%)}

.cta{left:221px;top:2950px;width:793px;height:168px;background:linear-gradient(180deg,#fff,#faf3f0 50%,#fff)}
.cta h2{position:absolute;left:107px;top:36px;font-family:var(--serif);font-weight:700;font-size:28px;line-height:30px}
.cta h2 em{font-style:normal;color:var(--red)}
.cta .btn{position:absolute;left:611px;top:68px}

.footer{left:221px;top:3118px;width:774px;height:248px;background:#161616;color:#fff}
.footer .col-split{position:absolute;left:322px;top:0;width:1px;height:248px;background:#2c2c2c}
.f-logo{position:absolute;left:107px;top:54px;font-family:var(--serif);font-weight:700;font-size:15px;display:flex;align-items:center;gap:5px}
.f-logo i{width:10px;height:10px;border-radius:50%;background:var(--orange)}
.f-social{position:absolute;left:107px;top:88px;display:flex;gap:9px}
.f-social i{width:17px;height:17px;border-radius:50%;background:#3a3a3a}
.f-social i.on{background:var(--orange)}
.f-copy{position:absolute;left:107px;top:130px;font-size:7px;color:var(--orange)}
.f-col{position:absolute;width:140px}
.f-col h4{font-family:var(--serif);font-weight:600;font-size:12px;margin-bottom:8px}
.f-col a{display:block;color:#9a9a9a;font-size:7px;line-height:15px;text-decoration:none}
</style>
</head>
<body>

<div class="abs brand-mark"><i class="dot"></i><span>FORNACE</span></div>
<div class="abs divider" style="left:481px;top:108px"></div>
<div class="abs font-list" style="left:546px;top:100px">
  <div class="board-title">Fonts:</div>
  <p class="f1" style="margin-top:6px">Crimson Pro Bold</p>
  <p class="f2">Nunito Sans Semibold</p>
  <p class="f3">Nunito Sans Regular</p>
</div>
<div class="abs divider" style="left:760px;top:108px"></div>
<div class="abs" style="left:826px;top:100px">
  <div class="board-title">Colors:</div>
  <div class="swatches" style="margin-top:8px">
    <div class="swatch"><i style="background:#1e1e1e"></i>#1e1e1e</div>
    <div class="swatch"><i style="background:#be1622"></i>#be1622</div>
    <div class="swatch"><i style="background:#ed691c"></i>#ed691c</div>
    <div class="swatch"><i style="background:#fdf3ee;box-shadow:0 0 0 1px #f0e2db"></i>#fdf3ee</div>
  </div>
</div>

<div class="abs page"></div>

<header class="abs nav">
  <div class="nav-logo"><i></i>FORNACE</div>
  <nav class="nav-links">
    <span>Home</span><span>About Us</span><span>Portfolio</span><span>Support</span><span>Quote</span>
    <a class="btn btn-solid" href="#">Contact Us</a>
    <div class="socials"><i></i><i></i><i></i></div>
  </nav>
</header>

<div class="abs photo hero-photo" role="img" aria-label="Friends gathered around an outdoor table while a man grills on a kamado grill by a lake"></div>
<div class="abs hero-card">
  <h1>The Ultimate<br>BBQ Experience</h1>
  <a class="btn btn-line" href="#">Free Quote</a>
  <svg width="18" height="14" viewBox="0 0 18 14" style="margin-left:10px;vertical-align:middle"><path d="M16 2 C12 4 10 8 4 10 M4 10 L7 7 M4 10 L8 12" stroke="#1e1e1e" stroke-width="1.2" fill="none"/></svg>
</div>

<section class="abs feature"></section>
<div class="abs photo grill-photo" role="img" aria-label="Black ceramic kamado grill on a stand"></div>
<div class="abs feature-text">
  <h2 class="title">An Fornace Grill<br>For Everyone</h2>
  <p class="body-s" style="margin-top:14px">At vero eos et accusamus et iusto odio dignissimos ducimus qui blanditiis praesentium aterat voluptatum <b style="color:#1e1e1e">deleniti atque corrupti quos dolores et quas</b> molestias excepturi sint occaecati</p>
  <ul class="ticks">
    <li><svg width="10" height="10"><circle cx="5" cy="5" r="4.2" fill="none" stroke="#be1622"/><path d="M3 5 L4.5 6.5 L7 3.8" stroke="#be1622" fill="none"/></svg>Heat Insulation Handle</li>
    <li><svg width="10" height="10"><circle cx="5" cy="5" r="4.2" fill="none" stroke="#be1622"/><path d="M3 5 L4.5 6.5 L7 3.8" stroke="#be1622" fill="none"/></svg>Adjustable top damper maintains airflow</li>
    <li><svg width="10" height="10"><circle cx="5" cy="5" r="4.2" fill="none" stroke="#be1622"/><path d="M3 5 L4.5 6.5 L7 3.8" stroke="#be1622" fill="none"/></svg>Bottom damper to control airflow for temperature</li>
    <li><svg width="10" height="10"><circle cx="5" cy="5" r="4.2" fill="none" stroke="#be1622"/><path d="M3 5 L4.5 6.5 L7 3.8" stroke="#be1622" fill="none"/></svg>Thermometer - to see how temperature changes</li>
  </ul>
  <p class="body-s">Lorem ipsum dolor sit amet, consectetur adipiscing elit, sed do eiusmod tempor incididunt ut labore et</p>
</div>

<section class="abs dark"></section>
<div class="abs dark-text">
  <h2 class="title">An Fornace Grill<br>For Everyone</h2>
  <p class="body-s" style="margin-top:14px">At vero eos et accusamus et iusto odio dignissimos ducimus qui blanditiis praesentium aterat</p>
  <ul class="ticks">
    <li><svg width="10" height="10"><circle cx="5" cy="5" r="4.2" fill="none" stroke="#ed691c"/><path d="M3 5 L4.5 6.5 L7 3.8" stroke="#ed691c" fill="none"/></svg>Heat Insulation Handle</li>
    <li><svg width="10" height="10"><circle cx="5" cy="5" r="4.2" fill="none" stroke="#ed691c"/><path d="M3 5 L4.5 6.5 L7 3.8" stroke="#ed691c" fill="none"/></svg>Adjustable top damper maintains airflow</li>
    <li><svg width="10" height="10"><circle cx="5" cy="5" r="4.2" fill="none" stroke="#ed691c"/><path d="M3 5 L4.5 6.5 L7 3.8" stroke="#ed691c" fill="none"/></svg>Bottom damper to control airflow for temperature</li>
  </ul>
  <p class="body-s">Lorem ipsum dolor sit amet, consectetur adipiscing elit, sed do eiusmod tempor incididunt ut labore et</p>
  <a class="btn btn-solid" href="#" style="margin-top:22px">Contact Us</a>
</div>
<div class="abs photo dark-photo" role="img" aria-label="Open kamado grill lid with steaks searing on the grate"></div>

<div class="abs section-head" style="top:1752px"><i></i><h2>Fornace Portfolio</h2></div>
<div class="abs card" style="left:241px"><div class="product" role="img" aria-label="Product photo: grill tongs, fork and spatula set"></div><span class="tag">FORNACE</span></div>
<div class="abs card" style="left:434px"><div class="product" role="img" aria-label="Product photo: BBQ tool set in a carry case"></div><span class="tag">FORNACE</span></div>
<div class="abs card" style="left:628px"><div class="product" role="img" aria-label="Product photo: compact kamado grill"></div><span class="tag">FORNACE</span></div>
<div class="abs card" style="left:821px"><div class="product" role="img" aria-label="Product photo: silicone basting brush"></div><span class="tag">FORNACE</span></div>
<div class="abs dots"><i></i><i class="on"></i><i></i></div>

<div class="abs mission-strip"></div>
<div class="abs photo mission-photo" role="img" aria-label="Hands turning meat on an open kamado grill outdoors"></div>
<section class="abs mission center-block">
  <i class="mk" style="background:#fff"></i>
  <h2>Fornace Mission</h2>
  <p>Lorem ipsum dolor sit amet, consectetur adipiscing elit, sed do eiusmod tempor incididunt ut labore et dolore magna aliqua. Quis ipsum suspendisse ultrices.</p>
  <p>Sed ut perspiciatis unde omnis iste natus error sit voluptatem accusantiumet doloremque laudantium, totam rem aperiam, alquae ab illo inventore veritatis et quasi architecto beatae Nemo enim ipsam voluptatem quia volupt daspernatur at.</p>
  <a class="btn btn-white" href="#" style="margin-top:16px">Contact Us</a>
</section>

<section class="abs values center-block">
  <i class="mk" style="background:var(--orange)"></i>
  <h2>Fornace Values</h2>
  <p>Lorem ipsum dolor sit amet, consectetur adipiscing elit, sed do eiusmod tempor incididunt ut labore et dolore magna aliqua. Quis ipsum suspendisse ultrices.</p>
  <p>Sed ut perspiciatis unde omnis iste natus error sit voluptatem accusantiumet doloremque laudantium, totam rem aperiam, alquae ab illo inventore veritatis et quasi architecto beatae Nemo enim ipsam voluptatem quia volupt daspernatur at.</p>
  <a class="btn btn-line" href="#" style="margin-top:16px">Free Quote</a>
</section>
<div class="abs photo values-photo" role="img" aria-label="Friends relaxing outdoors beside a kamado grill"></div>

<section class="abs cta">
  <h2>Need Unique Tools<br>For Your <em>BBQ</em> Party?</h2>
  <a class="btn btn-solid" href="#">Contact Us</a>
</section>

<footer class="abs footer">
  <div class="col-split"></div>
  <div class="f-logo"><i></i>FORNACE</div>
  <div class="f-social"><i></i><i class="on"></i><i></i></div>
  <div class="f-copy">© 2022 Fornace</div>
  <div class="f-col" style="left:454px;top:44px"><h4>About Company</h4><a>Our Story</a><a>Our Mission &amp; Values</a></div>
  <div class="f-col" style="left:616px;top:44px"><h4>Helpful Links</h4><a>Portfolio</a><a>About Us</a><a>Products &amp; Services</a></div>
  <div class="f-col" style="left:454px;top:130px"><h4>Support Center</h4><a>Request a Quote</a><a>Contact Us</a><a>Privacy Policy</a></div>
  <div class="f-col" style="left:616px;top:130px"><h4>Contact Us</h4><a>+1 555 010 0199</a><a>info@fornace-grills.com</a></div>
</footer>

</body>
</html>
```